Business Card Design

Business card design.

Business card is to have logo, website address and email address.

Website is www.brightkettle.ie
Email is info@brightkettle.ie
Logo uploaded

I have ordered Business Card Printing via Print Harbor, the Double-sided colour printed option with gloss finish.

Industry/Entity Type

Business

```html
<!DOCTYPE html>
<html lang="en">
<head>
<meta charset="utf-8">
<title>Bright Kettle Business Card</title>
<link rel="stylesheet" href="https://fonts.googleapis.com/css2?family=Arimo:wght@400;700&display=swap">
<style>
  :root {
    --page: #ffffff;
    --frame: #1a1a1a;
    --ink: #111111;
    --brand-red: #e00000;
    --panel-top: #ff6464;
    --panel-mid: #ff0a0a;
    --panel-bottom: #d80000;
    --card-line: #333333;
    --on-red: #ffffff;
  }
  * { box-sizing: border-box; margin: 0; padding: 0; }
  html, body { width: 991px; height: 1200px; overflow: hidden; }
  body {
    background: var(--page);
    font-family: "Arimo", Arial, sans-serif;
    position: relative;
  }
  .canvas-frame {
    position: absolute; inset: 0;
    border: 1px solid var(--frame);
  }
  .card {
    position: absolute;
    border: 1px solid var(--card-line);
    background: var(--page);
    overflow: hidden;
  }

  /* Front side */
  .card-front {
    left: 462px; top: 193px; width: 415px; height: 260px;
    display: flex; flex-direction: column; align-items: center; justify-content: center;
    gap: 14px;
  }
  .brand-mark {
    display: flex; align-items: center; gap: 12px;
  }
  .brand-dot {
    width: 46px; height: 46px; border-radius: 50%;
    background: var(--brand-red);
  }
  .brand-name {
    font-weight: 700; font-size: 33px; color: var(--ink);
    letter-spacing: 0.5px;
  }

  /* Back side */
  .card-back {
    left: 110px; top: 640px; width: 670px; height: 419px;
    display: flex;
  }
  .logo-strip {
    width: 232px; height: 100%;
    display: flex; align-items: center; justify-content: center;
    background: var(--page);
  }
  .logo-strip .brand-mark {
    transform: rotate(-90deg);
    white-space: nowrap;
  }
  .logo-strip .brand-dot { width: 40px; height: 40px; }
  .logo-strip .brand-name { font-size: 30px; }
  .details-panel {
    flex: 1; position: relative;
    background: linear-gradient(180deg, var(--panel-top) 0%, var(--panel-mid) 45%, var(--panel-bottom) 100%);
    color: var(--on-red);
    text-align: right;
    padding: 52px 40px 0 0;
  }
  .holder-name { font-weight: 700; font-size: 38px; }
  .holder-phone { font-weight: 700; font-size: 19px; margin-top: 14px; padding-right: 20px; }
  .contact-list { margin-top: 92px; font-weight: 700; font-size: 21px; line-height: 1.75; }
  .contact-label { margin-right: 10px; }
</style>
</head>
<body>
  <div class="canvas-frame"></div>

  <section class="card card-front" aria-label="Card front">
    <div class="brand-mark">
      <span class="brand-dot"></span>
      <span class="brand-name">BRIGHTKETTLE.IE</span>
    </div>
  </section>

  <section class="card card-back" aria-label="Card back">
    <div class="logo-strip">
      <div class="brand-mark">
        <span class="brand-dot"></span>
        <span class="brand-name">BRIGHTKETTLE.IE</span>
      </div>
    </div>
    <div class="details-panel">
      <p class="holder-name">Sam Rowe</p>
      <p class="holder-phone"><span class="contact-label">m.</span>+44 418226053</p>
      <div class="contact-list">
        <p><span class="contact-label">e.</span>info@brightkettle.ie</p>
        <p><span class="contact-label">w.</span>www.www.brightkettle.ie</p>
      </div>
    </div>
  </section>
</body>
</html>
```